Lotus Leaf Kitchen Road Billboard

Road Billboard I need all of this information on it
Authentic Thai Food Bangkok Style
6.5 Miles on the right
4126 Maple Ridge Rd Otto NC
828-555-4172

```html
<!DOCTYPE html>
<html lang="en">
<head>
<meta charset="utf-8">
<title>Lotus Leaf Kitchen Road Billboard</title>
<link href="https://fonts.googleapis.com/css2?family=Archivo+Black&family=Oswald:wght@500;700&display=swap" rel="stylesheet">
<style>
  :root {
    --stage: #cccccc;
    --black: #000000;
    --band: #e6e6e6;
    --gold: #d9a70f;
    --yellow: #ffff00;
    --white: #ffffff;
    --ember: #e0701a;
    --flame: #f5a623;
  }
  html, body {
    margin: 0;
    width: 1200px;
    height: 690px;
    overflow: hidden;
    background: var(--stage);
  }
  .billboard {
    position: absolute;
    left: 67px;
    top: 67px;
    width: 1067px;
    height: 555px;
    background: var(--black);
    overflow: hidden;
    font-family: "Archivo Black", "Arial Black", sans-serif;
  }
  .contact-band {
    position: absolute;
    left: 0; top: 462px;
    width: 100%; height: 93px;
    background: var(--band);
  }
  .artwork {
    position: absolute;
    left: 0; top: 0;
    width: 1067px; height: 555px;
  }
  .gold-text {
    background: linear-gradient(90deg, var(--gold) 0%, var(--yellow) 70%);
    -webkit-background-clip: text;
    background-clip: text;
    color: transparent;
    white-space: nowrap;
    position: absolute;
    left: 30px;
    margin: 0;
    line-height: 1;
  }
  .headline-small { top: 28px; font-size: 50px; letter-spacing: 4px; }
  .headline-main  { top: 82px; font-size: 100px; letter-spacing: -1px; }
  .headline-style { top: 185px; font-size: 62px; letter-spacing: -0.5px; }
  .directions {
    position: absolute;
    left: 26px; top: 345px;
    margin: 0;
    white-space: nowrap;
    color: var(--black);
    line-height: 1;
  }
  .directions .distance { font-size: 46px; letter-spacing: -1px; }
  .directions .side {
    font-family: "Oswald", sans-serif;
    font-weight: 500;
    font-size: 36px;
    letter-spacing: 1px;
    margin-left: 6px;
  }
  .address {
    position: absolute;
    left: 26px; top: 412px;
    display: flex; align-items: center; gap: 22px;
    color: var(--white);
    font-family: "Oswald", sans-serif;
    font-weight: 700;
    font-size: 30px;
    margin: 0;
    white-space: nowrap;
  }
  .phone {
    position: absolute;
    left: 26px; top: 468px;
    display: flex; align-items: center; gap: 38px;
    color: var(--black);
    font-size: 76px;
    letter-spacing: -1px;
    line-height: 1;
    margin: 0;
    white-space: nowrap;
  }
  .brand-name {
    position: absolute;
    left: 820px; top: 138px;
    width: 240px;
    text-align: center;
    color: var(--white);
    font-family: "Oswald", sans-serif;
    font-weight: 500;
    font-size: 28px;
    margin: 0;
    white-space: nowrap;
  }
</style>
</head>
<body>
  <section class="billboard">
    <div class="contact-band"></div>

    <svg class="artwork" viewBox="0 0 1067 555" xmlns="http://www.w3.org/2000/svg">
      <defs>
        <radialGradient id="wok-fire" cx="0.45" cy="0.55" r="0.6">
          <stop offset="0" stop-color="#f7b744"/>
          <stop offset="0.35" stop-color="#d8621a"/>
          <stop offset="0.7" stop-color="#3a1a08"/>
          <stop offset="1" stop-color="#0b0604"/>
        </radialGradient>
        <linearGradient id="arrow-fill" x1="0" x2="1">
          <stop offset="0" stop-color="#d9a70f"/>
          <stop offset="0.75" stop-color="#ffff00"/>
        </linearGradient>
      </defs>
      <circle cx="935" cy="187" r="418" fill="#e6e6e6"/>
      <circle cx="935" cy="187" r="402" fill="url(#wok-fire)"
              role="img" aria-label="Photo of a flaming wok tossing shrimp, broccoli and vegetables"/>
      <polygon class="direction-arrow" fill="url(#arrow-fill)"
               points="0,342 499,342 499,307 610,370 499,433 499,398 0,398"/>
    </svg>

    <p class="brand-name">Lotus Leaf Kitchen</p>

    <h1 class="gold-text headline-small">AUTHENTIC</h1>
    <p class="gold-text headline-main">THAI FOOD</p>
    <p class="gold-text headline-style">BANGKOK STYLE</p>

    <p class="directions"><span class="distance">6.5 Miles</span><span class="side">ON THE RIGHT</span></p>

    <p class="address">
      <svg width="34" height="34" viewBox="0 0 34 34" aria-hidden="true">
        <path d="M10 2a8 8 0 0 1 8 8c0 6-8 14-8 14S2 16 2 10a8 8 0 0 1 8-8z" fill="none" stroke="#fff" stroke-width="3"/>
        <circle cx="10" cy="10" r="3" fill="#fff"/>
        <path d="M4 26l12 6 16-4-8-8" fill="none" stroke="#fff" stroke-width="3"/>
      </svg>
      4126 MAPLE RIDGE RD OTTO NC
    </p>

    <p class="phone">
      <svg width="88" height="58" viewBox="0 0 88 58" aria-hidden="true">
        <path d="M4 14c0-10 80-10 80 0v6H64v-6H24v6H4z" fill="#000"/>
        <path d="M26 18h36l14 30v8H12v-8z" fill="#000"/>
        <circle cx="44" cy="38" r="10" fill="#e6e6e6"/>
        <circle cx="44" cy="38" r="5" fill="#000"/>
      </svg>
      828-555-4172
    </p>
  </section>
</body>
</html>
```